KORVELTA Corporate Business Card

Modern business card design for company which focuses in the areas of Staffing, IT Consulting & Data Services. Please note: We are no longer using the IT subscript on the logo. All designs should have IT subscript removed.
Website: www.korveltait.example

```html
<!DOCTYPE html>
<html lang="en">
<head>
<meta charset="utf-8">
<title>KORVELTA Business Card</title>
<link rel="stylesheet" href="https://fonts.googleapis.com/css2?family=Lato:wght@400;700;900&display=swap">
<style>
  :root {
    --stage: #d6d6d6;
    --card: #161616;
    --blue: #1e9ad6;
    --blue-deep: #0a5c96;
    --white: #ffffff;
  }
  html, body {
    margin: 0;
    padding: 0;
    width: 1000px;
    height: 1200px;
    overflow: hidden;
    background: var(--stage);
    font-family: "Lato", Arial, sans-serif;
  }
  .canvas { position: relative; width: 1000px; height: 1200px; }
  .card {
    position: absolute;
    background: var(--card);
    overflow: hidden;
    box-shadow: 0 10px 28px rgba(0,0,0,0.35);
  }
  .card-front { left: 111px; top: 120px; width: 777px; height: 447px; }
  .card-back  { left: 109px; top: 633px; width: 782px; height: 447px; }

  .brand {
    position: absolute;
    display: flex;
    align-items: center;
    color: var(--blue);
    font-weight: 900;
    letter-spacing: 1px;
    line-height: 1;
  }
  .brand-square { background: var(--blue); flex: none; }
  .card-front .brand { left: 71px; top: 200px; font-size: 50px; gap: 10px; }
  .card-front .brand-square { width: 40px; height: 40px; }
  .card-back .brand { left: 159px; top: 186px; font-size: 90px; gap: 16px; }
  .card-back .brand-square { width: 72px; height: 72px; }

  .divider {
    position: absolute;
    left: 393px; top: 124px;
    width: 2px; height: 199px;
    background: var(--blue-deep);
  }
  .contact { position: absolute; left: 432px; top: 118px; color: var(--white); }
  .contact-name {
    margin: 0;
    color: var(--blue);
    font-size: 24px;
    font-weight: 700;
    letter-spacing: 0.3px;
  }
  .contact-role { margin: 2px 0 14px; font-size: 19px; }
  .contact-address { margin: 0 0 12px; font-size: 19px; line-height: 28px; }
  .contact-list { list-style: none; margin: 0; padding: 0; font-size: 19px; }
  .contact-list li { display: flex; align-items: center; gap: 10px; height: 28px; }
  .contact-list svg { width: 17px; height: 17px; flex: none; }

  .front-band { position: absolute; left: 0; top: 392px; }
  .office-hours {
    position: absolute;
    left: 395px; top: 392px;
    width: 382px; height: 55px;
    display: flex; align-items: center; justify-content: center;
    color: var(--white);
    font-size: 19px;
  }

  .back-url {
    position: absolute;
    left: 0; right: 0; top: 391px;
    text-align: center;
    color: var(--white);
    font-size: 20px;
  }
  .back-bar {
    position: absolute;
    left: 302px; top: 431px;
    width: 180px; height: 16px;
    background: var(--blue);
  }
</style>
</head>
<body>
<div class="canvas">
  <section class="card card-front">
    <div class="brand"><span class="brand-square"></span>KORVELTA</div>
    <div class="divider"></div>
    <div class="contact">
      <h1 class="contact-name">DORIAN HALE</h1>
      <p class="contact-role">Owner</p>
      <p class="contact-address">418 Alder Ave, Brookhaven<br>IN 47190, USA</p>
      <ul class="contact-list">
        <li>
          <svg viewBox="0 0 24 24" aria-hidden="true"><path fill="#1e9ad6" d="M6.6 10.8a15.1 15.1 0 0 0 6.6 6.6l2.2-2.2a1 1 0 0 1 1-.25 11.4 11.4 0 0 0 3.6.57 1 1 0 0 1 1 1V20a1 1 0 0 1-1 1A17 17 0 0 1 3 4a1 1 0 0 1 1-1h3.5a1 1 0 0 1 1 1c0 1.25.2 2.45.57 3.57a1 1 0 0 1-.25 1z"/></svg>
          812-555-0142
        </li>
        <li>
          <svg viewBox="0 0 24 24" aria-hidden="true"><path fill="#1e9ad6" d="M2 5h20v14H2z"/><path fill="none" stroke="#161616" stroke-width="2" d="M2 5l10 8 10-8"/></svg>
          contactus@korveltait.example
        </li>
        <li>
          <svg viewBox="0 0 24 24" aria-hidden="true" fill="none" stroke="#1e9ad6" stroke-width="1.8"><circle cx="12" cy="12" r="9.5"/><ellipse cx="12" cy="12" rx="4.2" ry="9.5"/><path d="M2.5 12h19M4 7h16M4 17h16"/></svg>
          www.korveltait.example
        </li>
      </ul>
    </div>
    <svg class="front-band" width="777" height="55" viewBox="0 0 777 55" aria-hidden="true">
      <polygon points="0,32 388,32 376,55 0,55" fill="#1e9ad6"/>
      <polygon points="426,0 777,0 777,55 372,55" fill="#0a5c96"/>
    </svg>
    <div class="office-hours">Office Hours: 8am-5pm EST</div>
  </section>

  <section class="card card-back">
    <div class="brand"><span class="brand-square"></span>KORVELTA</div>
    <div class="back-url">www.korveltait.example</div>
    <div class="back-bar"></div>
  </section>
</div>
</body>
</html>
```